5 Years of Lunemar Research

This is a book cover for a new research book that will include 5 years of clinical case studies showing patients' dramatic health improvements from mental illness, chronic inflammatory conditions, cancer, and injury, all following concentrated chiropractic care at Lunemar Health Institute. Our logo needs to be incorporated into the design subtly.
Please USE our website as reference to our facilty and design preferences: https://lunemarhealth-example.com/
Please USE information from the Internationally Published Research tab, which shows all of the cases that will be included in this book, plus a case on reversing cerebral palsy that will be published in a few weeks.

This needs to be a design made for a 8.5x11 sized book.

Target Market(s)

People with chronic disease or health problem

Industry/Entity Type

Healthcare

Font styles to use
Serif
Other font styles liked:
• Avenir, Graphic, Optimum, Century Gothic

Colors
00AB8E
00BBA5
67D7C9
C6EFE9
E9F9F6
FFC000
F8CF3A
FAE287
FDF2CF
FEFAEE

Requirements
Must have
• It must be profession. Our colors are dark green / gold / white.
Nice to have
• I would like to see something that is eye-catching and would encourage a person to buy and read this book. Including spine/brain/chiropractic images is optimal.

```html
<!DOCTYPE html>
<html lang="en">
<head>
<meta charset="utf-8">
<title>5 Years of Lunemar Research – Book Cover</title>
<link rel="stylesheet" href="https://fonts.googleapis.com/css2?family=Cinzel:wght@400;500&family=Marcellus&display=swap">
<style>
  :root {
    --page: #ffffff;
    --cover-green: #036a3b;
    --gold: #cf9236;
    --white: #ffffff;
    --rule: rgba(255,255,255,0.85);
  }
  * { margin: 0; padding: 0; box-sizing: border-box; }
  html, body { width: 1200px; height: 1200px; overflow: hidden; background: var(--page); }
  .canvas { position: relative; width: 1200px; height: 1200px; }
  .jacket {
    position: absolute; left: 33px; top: 176px; width: 1128px; height: 806px;
    background: var(--cover-green); overflow: hidden;
  }
  .spine-edge { position: absolute; top: 0; bottom: 0; width: 1px; background: var(--rule); }
  .spine-edge.left { left: 542px; }
  .spine-edge.right { left: 584px; }

  /* back cover */
  .back { position: absolute; left: 0; top: 0; width: 542px; height: 100%; font-family: "Cinzel", serif; color: var(--white); }
  .back-title {
    position: absolute; left: 0; top: 40px; width: 100%; text-align: center;
    color: var(--gold); font-weight: 400; font-size: 44px; line-height: 38px; font-variant: small-caps;
  }
  .back-copy { position: absolute; left: 59px; top: 146px; width: 432px; font-size: 13.2px; line-height: 19px; letter-spacing: 0.02em; }
  .back-copy p { margin-bottom: 14px; }
  .back-copy ul { list-style: none; margin-bottom: 14px; }
  .back-copy li { margin-bottom: 4px; }
  .back-copy li::before { content: "l"; font-size: 10px; margin-right: 8px; }
  .back-copy .first { margin-bottom: 14px; }

  .imprint { display: flex; align-items: center; gap: 6px; font-family: "Cinzel", serif; font-weight: 500; color: var(--white); }
  .imprint .dot { width: 10px; height: 10px; border-radius: 50%; background: var(--white); }
  .imprint-back { position: absolute; left: 64px; top: 718px; font-size: 18px; }

  /* spine */
  .spine {
    position: absolute; left: 543px; top: 0; width: 41px; height: 100%;
    font-family: "Cinzel", serif; color: var(--white); font-size: 19px;
  }
  .spine-text { position: absolute; left: 9px; writing-mode: vertical-rl; white-space: nowrap; }
  .spine-title { top: 74px; }
  .spine-author { top: 445px; font-size: 17px; }

  /* front cover */
  .front { position: absolute; left: 585px; top: 0; width: 543px; height: 100%; text-align: center; }
  .front-title { font-family: "Cinzel", serif; font-weight: 400; color: var(--gold); }
  .front-title span { display: block; position: absolute; left: 0; width: 100%; white-space: nowrap; }
  .title-years { top: 40px; font-size: 138px; line-height: 140px; letter-spacing: -0.02em; }
  .title-of { top: 168px; font-size: 66px; line-height: 70px; color: var(--white); }
  .title-name { top: 222px; font-size: 100px; line-height: 120px; letter-spacing: -0.04em; }
  .title-research { top: 336px; font-size: 94px; line-height: 100px; letter-spacing: -0.03em; }
  .front-rule { position: absolute; left: 56px; width: 440px; height: 1px; background: var(--rule); }
  .front-rule.top { top: 464px; }
  .front-rule.bottom { top: 585px; }
  .subtitle {
    position: absolute; left: 0; top: 484px; width: 100%; font-family: "Marcellus", serif;
    color: var(--white); font-size: 39px; line-height: 42px; letter-spacing: 0.04em;
  }
  .imprint-front { position: absolute; left: 0; width: 100%; top: 640px; justify-content: center; font-size: 20px; }
  .author-lead {
    position: absolute; left: 0; top: 712px; width: 100%; font-family: "Marcellus", serif;
    color: var(--white); font-size: 25px; letter-spacing: 0.05em;
  }
  .coauthors {
    position: absolute; left: 0; top: 752px; width: 100%; display: flex; justify-content: center;
    font-family: "Marcellus", serif; color: var(--white); font-size: 17px; letter-spacing: 0.05em;
  }
  .coauthors span { padding: 0 12px; }
  .coauthors span + span { border-left: 1px solid var(--rule); }
</style>
</head>
<body>
<div class="canvas">
  <div class="jacket">
    <section class="back">
      <h2 class="back-title">5 Years of<br>Lunemar Research</h2>
      <div class="back-copy">
        <p>Many Christian singles enter dating with sincere faith and good intentions. Yet they still end up confused, drained, or hurt. Too often, spiritual language is mistaken for emotional health, attraction is confused with compatibility, and red flags are ignored in the name of grace.</p>
        <p>This practical Christian dating guide helps you slow down, see clearly, and discern wisely before attachment clouds your judgment.</p>
        <p>Inside, you’ll learn how to:</p>
        <p class="first">Recognize red flags that signal emotional immaturity, manipulation, or unhealthy attachment</p>
        <ul>
          <li>Identify green flags that point to humility, stability, and relational health</li>
          <li>Understand the difference between attraction, chemistry, and true compatibility</li>
          <li>Discern character over charm, even when someone appears spiritual</li>
          <li>Evaluate patterns, not promises</li>
        </ul>
        <p>Rather than offering shallow advice like “just pray,” “as long as you have a peace...,</p>
      </div>
      <div class="imprint imprint-back"><span class="dot"></span>LUNEMAR</div>
    </section>

    <div class="spine-edge left"></div>
    <div class="spine-edge right"></div>
    <section class="spine">
      <span class="spine-text spine-title">5 Years of Lunemar Research</span>
      <span class="spine-text spine-author">Dr. Helena Varrow BS DC NTP</span>
    </section>

    <section class="front">
      <h1 class="front-title">
        <span class="title-years">5 YEARS</span>
        <span class="title-of">OF</span>
        <span class="title-name">LUNEMAR</span>
        <span class="title-research">RESEARCH</span>
      </h1>
      <div class="front-rule top"></div>
      <p class="subtitle">LIFE CHANGING<br>CHIROPRACTIC CARE</p>
      <div class="front-rule bottom"></div>
      <div class="imprint imprint-front"><span class="dot"></span>LUNEMAR</div>
      <p class="author-lead">DR. HELENA VARROW BS DC NTP</p>
      <p class="coauthors"><span>DR. AABBCCDD</span><span>DR. AABBCCDD</span><span>DR. AABBCCDD</span></p>
    </section>
  </div>
</div>
</body>
</html>
```